Poem Handwritten by Veteran while in the jungle of Vietnam

My parents are celebrating their 50th wedding anniversary this year. I wanted to give them a very memorable gift. On my parents 2nd anniversary, my father was stationed in Vietnam. On that night he was in the jungle waiting till morning and wrote a poem to my mother using his pant leg as paper. I would like this poem to typographically designed to be framed and hung on the wall.

I have attached a picture of the poem below. It will need to be 11x14 when printed for framing. It would be great if there was background or artwork to make it more visually interesting, perhaps in a watercolor. My parents have a transitional style. I have attached some possible color schemes as well. Cool greens, blue, neutral grays, with hints of berries or highlights of yellow. These are just a guide, I would be open to your interpretations.

Thank you for your help. This will hopefully be a gift they will truly treasure as much as the poem itself.

Target Market(s)

My parents who are excited to be celebrating their 50th wedding anniversary. It should have a transitional, mature style.

Font styles to use
Serif
Script

Requirements
Must have
• The poem, typographically designed. There can be a mix of fonts, but legibility is critically important.
• Now that some designs have come through I wanted to give some more guidance of what I'm looking for. I want something that feels sophisticated and artistic.
Nice to have
• A background or art work, using the color schemes attached as a guide. I am really liking the designs that have a full color landscape artwork in the background. The fonts should be elegant and formal. I really like the romantic, muted colors. I had trouble finding similar projects online in the style I wanted until I cam across wedding invites. Those seem to be the most applicable. I've added pictures of some so you can get a sense of what I'm looking for. I am really liking the jungle foliage, starry skies or sunrises.
Should not have
• Cartoon caricatures, fonts that are too illegible when printed. I'm not liking anything whimsical. I don't like the very bright colors for this project.

```html
<!DOCTYPE html>
<html lang="en">
<head>
<meta charset="utf-8">
<title>Happy Anniversary Darling</title>
<link rel="stylesheet" href="https://fonts.googleapis.com/css2?family=Pinyon+Script&family=EB+Garamond:ital,wght@0,400;0,500;1,400&display=swap">
<style>
  :root {
    --page-bg: #6b6b6b;
    --night-deep: #05080f;
    --night-mid: #122545;
    --night-glow: #27497a;
    --ink-light: #f1f3f7;
    --gold: #d8b24a;
    --gold-soft: rgba(216, 178, 74, 0.35);
  }
  * { margin: 0; padding: 0; box-sizing: border-box; }
  html, body {
    width: 1200px;
    height: 1200px;
    overflow: hidden;
    background: var(--page-bg);
  }
  .poster {
    position: absolute;
    left: 146px;
    top: 22px;
    width: 908px;
    height: 1155px;
    overflow: hidden;
    color: var(--ink-light);
  }
  .poster__backdrop {
    position: absolute;
    inset: 0;
    background:
      radial-gradient(ellipse 55% 45% at 62% 45%, var(--night-glow) 0%, rgba(39,73,122,0) 70%),
      linear-gradient(180deg, var(--night-deep) 0%, var(--night-mid) 45%, #0f1f3a 70%, var(--night-deep) 100%);
  }
  .poster__frame {
    position: absolute;
    inset: 0;
  }
  .ornament {
    position: absolute;
    background: radial-gradient(ellipse at center, var(--gold-soft) 0%, rgba(216,178,74,0) 70%);
  }
  .ornament--top-left { left: 35px; top: 34px; width: 212px; height: 120px; }
  .ornament--bottom-right { left: 662px; top: 999px; width: 213px; height: 121px; }
  .title {
    position: absolute;
    left: 0;
    width: 100%;
    text-align: center;
    font-family: "Pinyon Script", cursive;
    font-weight: 400;
    color: #ffffff;
    line-height: 1;
  }
  .title--main { top: 118px; font-size: 98px; padding-left: 10px; }
  .title--name { top: 222px; font-size: 98px; padding-left: 10px; }
  .poem {
    position: absolute;
    top: 375px;
    width: 380px;
    text-align: center;
    font-family: "EB Garamond", serif;
    font-style: italic;
    font-size: 20px;
    line-height: 23px;
  }
  .poem--left { left: 87px; }
  .poem--right { left: 462px; }
  .poem__stanza { margin-bottom: 23px; }
  .dedication {
    position: absolute;
    left: 0;
    width: 100%;
    top: 1052px;
    text-align: center;
    font-family: "EB Garamond", serif;
    font-size: 15px;
    line-height: 21px;
    text-transform: uppercase;
    letter-spacing: 0.2px;
  }
</style>
</head>
<body>
  <main class="poster">
    <div class="poster__backdrop" role="img" aria-label="Moonlit starry night sky seen upward through silhouetted jungle trees, with a full moon in the upper right"></div>

    <svg class="poster__frame" width="908" height="1155" viewBox="0 0 908 1155" aria-hidden="true">
      <g stroke="var(--gold)" stroke-width="3" fill="none">
        <line x1="245" y1="36" x2="507" y2="36"/>
        <line x1="39" y1="154" x2="39" y2="416"/>
        <line x1="869" y1="736" x2="869" y2="1004"/>
        <line x1="402" y1="1118" x2="662" y2="1118"/>
      </g>
    </svg>
    <div class="ornament ornament--top-left" role="img" aria-label="Gold filigree corner ornament"></div>
    <div class="ornament ornament--bottom-right" role="img" aria-label="Gold filigree corner ornament"></div>

    <h1 class="title title--main">Happy Anniversary</h1>
    <p class="title title--name">Darling</p>

    <section class="poem poem--left">
      <p class="poem__stanza">Life’s journey began with a challenge,<br>It was heralded far and near.<br>The road led forever,<br>Its completion was known to be dear.</p>
      <p class="poem__stanza">From the garden of light it proceeded,<br>To the valley of shadows it led.<br>Thorns and thistles adorned it,<br>Past abyss and crevice is sped.</p>
      <p class="poem__stanza">The brave surged forward with courage,<br>The wise undaunted pressed on.<br>The mighty held high their banner,<br>We all awaited the dawn.</p>
      <p class="poem__stanza">Though the pitfalls and hazards were many,<br>The pathway was clear in view.<br>Straight and sure it glided,<br>Its course we knew to be true.</p>
      <p class="poem__stanza">I knew you, Sweetheart, beforehand,<br>So precious and sweet were you,<br>Our moments of bliss were priceless,<br>Each day brought us joy anew.</p>
      <p class="poem__stanza">The call to progression beckoned,<br>At last I would have my chance–</p>
    </section>

    <section class="poem poem--right">
      <p class="poem__stanza">To clasp you to me forever,<br>And seal our divine romance.</p>
      <p class="poem__stanza">I eagerly started the journey,<br>Though with sorrow, I left you behind.<br>With courage and faith I continued,<br>For I knew, that you later I’d find.</p>
      <p class="poem__stanza">I diligently search for you, Darling,<br>The roadway was both bleak and fair.<br>Though the years grew long in number,<br>I did not give up in despair.</p>
      <p class="poem__stanza">At last in the distance I saw you,<br>So beautiful, lovely, and sweet!<br>Your attention I struggled to capture,<br>Your love I wrested to meet.</p>
      <p class="poem__stanza">What rapture was mine in fulfilment,<br>As now together we stand.<br>To cherish and love each other,<br>While our plans and dreams expand.</p>
      <p class="poem__stanza">I love you, Darling, forever,<br>My life you have made replete.<br>Our eternal mansion beckons,<br>Your love has made it complete.</p>
    </section>

    <footer class="dedication">
      <p>20 July 1970, Monday, LZ Meridian</p>
      <p>Walter’s Anniversary Poem</p>
    </footer>
  </main>
</body>
</html>
```